Redesign of Real Estate Agency Website

We need a redesign for our real estate agency website. Please see attached creative brief.

Target Market(s)

Refer to creative brief.

Industry/Entity Type

Real Estate

Requirements
Must have
• Refer to creative brief.

```html
<!DOCTYPE html>
<html lang="en">
<head>
<meta charset="utf-8">
<title>Islandnest – Island Property &amp; Real Estate</title>
<link href="https://fonts.googleapis.com/css2?family=Arimo:wght@400;700&display=swap" rel="stylesheet">
<style>
:root{
  --navy:#0b3a8c;
  --blue:#1b67cf;
  --blue-light:#3d8be6;
  --panel:#d9e7f7;
  --panel-edge:#9dbde6;
  --ink:#1d1d1d;
  --muted:#555;
  --footer:#e9eff7;
  --white:#fff;
  --gold:#f3c21b;
  --badge:#1a1a1a;
}
*{box-sizing:border-box;margin:0;padding:0}
html,body{width:743px;height:1200px;overflow:hidden;background:var(--white)}
body{font-family:"Arimo",Arial,sans-serif;color:var(--ink);font-size:8px;line-height:1.35;position:relative}
.abs{position:absolute}
/* header */
.brand{left:32px;top:12px}
.brand-name{font-size:26px;font-weight:700;color:var(--blue);letter-spacing:-.5px;line-height:1}
.brand-tag{font-size:9px;font-weight:700;color:var(--navy);margin-top:3px}
.cart{right:30px;top:12px;font-size:8px;color:var(--muted);text-align:left}
.cart div{display:flex;align-items:center;gap:4px;margin-bottom:3px}
.cart i{width:7px;height:7px;border-radius:50%;border:1px solid var(--muted);display:inline-block}
.site-search{right:30px;top:46px;display:flex;gap:4px}
.site-search span{width:150px;height:15px;border:1px solid #aaa;display:block}
.site-search b{font-size:8px;font-weight:400;background:#eee;border:1px solid #aaa;padding:1px 6px}
/* nav */
.main-nav{left:32px;top:72px;width:683px;height:22px;background:linear-gradient(var(--blue-light),var(--blue));display:flex;align-items:center;border-radius:2px}
.main-nav a{color:var(--white);text-decoration:none;font-size:9px;font-weight:700;padding:0 8px;border-right:1px solid rgba(255,255,255,.5);line-height:22px}
.main-nav a.current{background:var(--navy);font-size:11px;padding:0 12px}
.main-nav a:last-child{border:0}
/* panels */
.panel{background:var(--panel);border:1px solid var(--panel-edge);border-radius:3px}
.panel-head{background:var(--white);margin:4px;padding:3px 5px;font-size:9px;font-weight:700;color:var(--navy);border-radius:2px}
.quick-search{left:34px;top:102px;width:176px;height:243px;padding-bottom:6px}
.select{margin:7px 10px;height:15px;background:var(--white);border:1px solid #98a9c2;font-size:8px;padding:2px 4px;position:relative;width:100px}
.select::after{content:"";position:absolute;right:3px;top:5px;border:3px solid transparent;border-top-color:#333}
.btn{display:block;background:linear-gradient(var(--blue-light),var(--navy));color:var(--white);font-weight:700;text-align:center;border-radius:3px}
.btn-search{margin:10px auto 6px;width:80px;height:20px;line-height:20px;font-size:11px}
.btn-adv{margin:0 auto;width:110px;height:16px;line-height:16px;font-size:9px}
.hero{left:216px;top:102px;width:499px;height:290px;background:linear-gradient(160deg,#8fb7cf 0%,#e9e2d4 45%,#6aa1c2 75%,#2f6f98 100%);border:1px solid #ccd}
.browse{left:34px;top:352px;width:176px;height:160px}
.browse ul{list-style:none;padding:4px 10px}
.browse li{color:var(--white);font-size:9px;margin:4px 0;padding-left:8px;position:relative}
.browse li::before{content:"";position:absolute;left:0;top:3px;border:3px solid transparent;border-left-color:var(--white)}
.browse-box{background:linear-gradient(var(--blue-light),var(--blue))}
.featured{left:216px;top:352px;width:499px;height:135px;background:var(--panel);border:1px solid var(--panel-edge);border-radius:3px}
.featured-title{position:absolute;left:50%;transform:translateX(-50%);top:-2px;background:var(--blue);color:var(--white);font-weight:700;font-size:9px;padding:4px 14px;border-radius:0 0 4px 4px}
.arrow{position:absolute;top:56px;border:8px solid transparent}
.arrow.prev{left:4px;border-right-color:var(--navy)}
.arrow.next{right:4px;border-left-color:var(--navy)}
.thumbs{position:absolute;left:28px;top:28px;display:flex;gap:8px}
.thumb{width:81px;font-size:7px;color:var(--ink)}
.thumb .pic{height:46px;background:linear-gradient(#7fb0d6,#c9b48e);margin-bottom:3px;border:1px solid #fff}
.thumb b{color:var(--navy)}
/* map */
.map{left:34px;top:515px;width:176px;height:225px;border:1px solid var(--panel-edge)}
.map h3{font-size:9px;color:var(--navy);text-align:center;margin-top:5px}
.map .radios{display:flex;justify-content:center;gap:10px;font-size:8px;margin:4px 0}
.map .radios i{display:inline-block;width:7px;height:7px;border-radius:50%;border:1px solid #555;margin-right:2px;vertical-align:-1px}
.map .map-area{margin:2px 14px;height:160px;background:linear-gradient(#eef3f9,#cfdbe9)}
.map a{display:block;font-size:8px;color:var(--blue);margin-left:18px;margin-top:3px}
/* listings */
.listing{top:492px;width:150px}
.listing h2{background:var(--blue);color:var(--white);font-size:11px;padding:4px 6px}
.listing .pic{height:100px;background:linear-gradient(#4f9ad8,#3fb3c9 60%,#cfe3ea);margin:3px 0}
.listing p{font-size:7.5px;margin-bottom:1px}
.listing .name{color:var(--blue);font-weight:700;font-size:8px;margin:3px 0}
.sale{left:228px}.rent{left:385px}
.award{left:598px;top:490px;width:108px;height:240px;background:var(--badge)}
/* services */
.services{left:230px;top:746px;width:470px}
.services h2{font-size:13px;color:var(--ink)}
.services h4{font-size:9px;margin:3px 0}
.services p{font-size:7.5px;line-height:1.45}
.services a{color:var(--blue)}
/* newsletter */
.newsletter{left:34px;top:756px;width:176px;height:80px;border:1px solid var(--panel-edge);background:var(--blue)}
.newsletter h3{background:var(--white);color:var(--navy);font-size:9px;padding:3px 5px;margin:3px}
.newsletter p{color:var(--white);font-size:7px;padding:0 6px}
.newsletter .field{display:flex;gap:3px;padding:4px 6px}
.newsletter .field span{background:var(--white);flex:1;height:13px;font-size:7px;padding:2px;color:#777}
.newsletter .field b{background:var(--navy);color:var(--white);font-size:7px;padding:2px 4px}
.newsletter .privacy{font-size:7px;color:var(--white);padding:0 6px}
.deals{left:68px;top:858px;width:110px;height:24px;background:var(--gold);border-radius:4px;font-size:9px;font-weight:700;color:var(--navy);text-align:center;line-height:24px}
.team{left:34px;top:895px;width:176px;height:66px;background:linear-gradient(90deg,#6c8fb8,#c9a88e,#6c8fb8)}
/* footer */
.footer{left:0;top:975px;width:743px;height:195px;background:var(--footer);border-top:1px solid var(--panel-edge)}
.footer-col{position:absolute;top:8px;font-size:7.5px;line-height:1.35}
.footer-col h3{font-size:11px;color:var(--navy);margin-bottom:4px}
.footer-col b{display:block}
.bottom-bar{left:0;top:1170px;width:743px;height:30px;background:linear-gradient(var(--blue),var(--navy));color:var(--white);font-size:8px;text-align:center;line-height:22px}
</style>
</head>
<body>
<header>
  <div class="abs brand"><div class="brand-name">Islandnest</div><div class="brand-tag">Island Property &amp; Real Estate</div></div>
  <div class="abs cart"><div><i></i>0 items in sales inquiry cart</div><div><i></i>0 items in rentals inquiry cart</div></div>
  <div class="abs site-search"><span></span><b>Search</b></div>
  <nav class="abs main-nav">
    <a class="current">Home</a><a>Property for Sale</a><a>Property for Rent</a><a>Contact Us</a><a>About Us</a><a>List Your Property</a><a>Property Buyer's Guide</a>
  </nav>
</header>

<section class="abs panel quick-search">
  <div class="panel-head">Quick Property Search</div>
  <div class="select">Buy Property</div>
  <div class="select">Property Type</div>
  <div class="select">Region</div>
  <div class="select">District</div>
  <div class="select">Minimum Bedrooms</div>
  <div class="select">Maximum Price (THB)</div>
  <span class="btn btn-search">Search</span>
  <span class="btn btn-adv">Advance Search</span>
</section>

<div class="abs hero" role="img" aria-label="Sea-view bedroom with large windows overlooking the ocean"></div>

<section class="abs panel browse browse-box">
  <div class="panel-head">Browse Property for Sale</div>
  <ul><li>Apartments &amp; Condos</li><li>Villas &amp; Houses</li><li>Land</li><li>Commercial</li><li>Property Buyer's Guide</li><li>Hot Properties &amp; Promotions</li></ul>
</section>

<section class="abs featured">
  <div class="featured-title">Featured Property</div>
  <span class="arrow prev"></span><span class="arrow next"></span>
  <div class="thumbs">
    <div class="thumb"><div class="pic" role="img" aria-label="Villa exterior"></div><b>Villa 22-15, Kamala</b><br>Bedrooms: 3<br>From THB 18,500,000</div>
    <div class="thumb"><div class="pic" role="img" aria-label="Villa with pool"></div><b>Villa 184, Surin</b><br>Bedrooms: 4<br>THB 150,000 /month</div>
    <div class="thumb"><div class="pic" role="img" aria-label="Villa garden"></div><b>Villa 194-215, Patong</b><br>Bedrooms: 3<br>THB 14,000,000</div>
    <div class="thumb"><div class="pic" role="img" aria-label="Hillside villa"></div><b>Villa 188-14, Rawai</b><br>Bedrooms: 5<br>THB 32,000,000</div>
    <div class="thumb"><div class="pic" role="img" aria-label="Apartment building"></div><b>Apt. 2771, Patong</b><br>Bedrooms: 1<br>THB 3,900,000</div>
  </div>
</section>

<section class="abs map">
  <h3>Search by Map</h3>
  <div class="radios"><span><i></i>Buy</span><span><i></i>Rent</span></div>
  <div class="map-area" role="img" aria-label="Map of the island divided into regions"></div>
  <a>View Large Map</a>
</section>

<article class="abs listing sale">
  <h2>Property For Sale</h2>
  <div class="pic" role="img" aria-label="Resort pool at the property"></div>
  <p class="name">The Harbour</p>
  <p><b>Type:</b> Apartment/Condo</p>
  <p><b>Price:</b> THB 7.6M – 25.89M</p>
  <p><b>Location:</b> Surin, West Coast</p>
  <p><b>Views:</b> Sea</p>
  <p>The Harbour is located directly above Surin Beach. Surin Beach is the heart of the five-star region on the west coast.</p>
</article>
<article class="abs listing rent">
  <h2>Property For Rent</h2>
  <div class="pic" role="img" aria-label="Resort pool at the property"></div>
  <p class="name">The Harbour</p>
  <p><b>Type:</b> Apartment/Condo</p>
  <p><b>Price:</b> THB 7.6M – 25.89M</p>
  <p><b>Location:</b> Surin, West Coast</p>
  <p><b>Views:</b> Sea</p>
  <p>The Harbour is located directly above Surin Beach. Surin Beach is the heart of the five-star region on the west coast.</p>
</article>

<div class="abs award" role="img" aria-label="Property award badge"></div>

<section class="abs services">
  <h2>The Services We Offer</h2>
  <h4>Comprehensive service with integrity:</h4>
  <p>Extensive selection of island properties for sale and rent.<br>
  Research and suggest properties that meet our clients' requirements.<br>
  Arrange property sales and rentals viewings.<br>
  Chauffer and escort clients throughout their property viewings.<br>
  Provide independent advice regarding buying and renting property on the island.<br>
  Offer unbiased legal information and can assist in appointing independent lawyers.<br>
  Provide the best possible deal for our clients by negotiating with sellers and developers.<br>
  Provide a comprehensive after-sales service by liaising with all parties involved.<br>
  Provide regular updates to clients on their property purchase.<br>
  Provide advice and support on all aspects of living on the island and in Thailand.</p>
  <h4 style="margin-top:6px">Why Use Islandnest Real Estate?</h4>
  <p>Islandnest Real Estate is one of the most experienced independent real estate agents focusing completely on the island.<br>
  Our team has lived on the island for a total of over 40 years and our experience with real estate exceeds 30 years, so we feel we are very well qualified to provide high quality services to our clients. <a>About us</a><br>
  Proven track record with many satisfied clients.</p>
</section>

<section class="abs newsletter">
  <h3>Get Our Newsletter</h3>
  <p>Get the latest island real estate news and deals every month.</p>
  <div class="field"><span>Your Email Here</span><b>Subscribe</b></div>
  <div class="privacy">Privacy &amp; Unsubscribe</div>
</section>
<div class="abs deals">Check out our hot deals</div>
<div class="abs team" role="img" aria-label="Photo of the agency team"></div>

<footer class="abs footer">
  <div class="footer-col" style="left:34px"><h3>Island Real Estate for Sale</h3>
  island property for sale index<br>search property for sale<br>apartments &amp; condos for sale<br>villas &amp; houses for sale<br>land for sale<br>commercial property for sale<br>luxury property for sale<br>island property for sale map<br>property buyer's guide<br>why buy on the island?<br>property ownership rights<br>property taxes &amp; fees<br>land titles<br>land units<br>property faq</div>
  <div class="footer-col" style="left:230px"><h3>Island Property for Rent</h3>
  island property for rent index<br>search property for rent<br>island holiday rentals<br>holiday villas<br>luxury villas<br>cheap villas<br>holiday apartments<br>holiday rentals booking guide<br>holiday rentals faq<br><b>Terms &amp; conditions</b>long-term rentals<br>long term villas &amp; houses<br>long-term apartments<br>property for rent map</div>
  <div class="footer-col" style="left:415px"><h3>Site Links</h3>
  islandnest real estate index<br>privacy policy<br>disclaimer<br>site map<br><h3 style="margin-top:6px">About islandnest real estate</h3>about us<br>contact us<br>find your property<br>selling your property</div>
  <div class="footer-col" style="left:590px"><h3>Island info</h3>
  island homepage<br>travel info<br>tours<br>dining &amp; nightlife<br>expats<br>directory<br>classified ads<br>hotels</div>
</footer>
<div class="abs bottom-bar">Island Real Estate from Islandnest | Copyright © Islandnest 2010. All Rights Reserved</div>
</body>
</html>
```